Pelbrooks Burgers and Tacos needs a new menu board design

We are a fast casual restaurant that sells burgers, tacos, wraps and other items. We have a California feel, sleek and modern, décor has photos of people like Vormack, Tessard, Brastow. Song list varies from Copper Lanterns, Amber Meridian, Corvanes, Halloway Brightmoor etc... Our main goal for this project is to clean up the look of our menu boards...make them easier to read and more reflective of the style of the restaurant. We also want to feature our combos which are our high profit items...think they should take up 30 to 40% of the space.

We have t-shirts that say "Don't Worry Be Hippy", "Carry Me Down Slowly", "Make Tacos Not War".

There is potential for other projects such as outdoor menu panels, paper menus, promotional items. I am attaching a layout of the menu panels as they appear now with dimensions. Also photos of the restaurant. We are not planning to use these same panels so please don't design around them...come up with your own ideas on this....there is a slightly curved background. We have a really good sign person that can customize if need be.

We have had this menu for a long time and it needs to be clean and sleek.

Target Market(s)

teenagers to 40+

Industry/Entity Type

Restaurant

Requirements
Must have
• Clean readable headers

```html
<!DOCTYPE html>
<html lang="en">
<head>
<meta charset="utf-8">
<title>Pelbrooks Burgers and Tacos — Combos</title>
<link rel="stylesheet" href="https://fonts.googleapis.com/css2?family=Damion&family=Ropa+Sans&family=Yellowtail&display=swap">
<style>
  :root {
    --stone: #6f7b72;
    --stone-dark: #5c665f;
    --stone-light: #879188;
    --card: rgba(214, 224, 218, 0.62);
    --ink: #24385a;
    --ink-soft: #3f5a80;
    --rose: #a9566f;
    --white: #ffffff;
  }
  * { margin: 0; padding: 0; box-sizing: border-box; }
  html, body { width: 1155px; height: 1200px; overflow: hidden; }
  body {
    position: relative;
    background:
      radial-gradient(ellipse at 25% 20%, var(--stone-light) 0%, transparent 55%),
      radial-gradient(ellipse at 80% 75%, var(--stone-light) 0%, transparent 50%),
      linear-gradient(160deg, var(--stone) 0%, var(--stone-dark) 100%);
    font-family: "Ropa Sans", "Arial Narrow", sans-serif;
    color: var(--ink);
  }
  .board-title {
    position: absolute;
    left: 0; width: 1155px; top: 6px;
    text-align: center;
    font-family: "Damion", cursive;
    font-size: 176px;
    line-height: 1.2;
    color: var(--white);
    text-shadow: -7px 5px 0 var(--rose);
    padding-left: 10px;
  }
  .divider {
    position: absolute;
    left: 576px; top: 246px;
    width: 3px; height: 714px;
    background: var(--white);
  }
  .combo {
    position: absolute;
    width: 434px; height: 148px;
    background: var(--card);
  }
  .combo-number {
    position: absolute;
    left: 5px; top: 15px;
    width: 17px; height: 25px;
    background: var(--rose);
    color: var(--white);
    font-family: Arial, sans-serif;
    font-size: 24px; line-height: 25px;
    text-align: center;
  }
  .combo-name {
    position: absolute;
    left: 56px; top: 10px;
    white-space: nowrap;
    font-size: 34px;
    font-weight: 700;
    color: var(--ink);
    -webkit-text-stroke: 0.6px var(--ink);
  }
  .combo-name .brand {
    font-family: "Yellowtail", cursive;
    font-weight: 400;
    font-size: 40px;
    margin-right: 6px;
  }
  .combo-sides {
    position: absolute;
    left: 0; width: 100%; top: 76px;
    text-align: center;
    font-size: 21px; line-height: 22px;
    color: var(--ink-soft);
  }
  .combo-extra {
    position: absolute;
    left: 0; width: 100%; top: 97px;
    text-align: center;
    font-size: 13px; line-height: 14px;
    color: var(--ink);
  }
  .combo-addon {
    position: absolute;
    left: 4px; top: 125px;
    font-size: 12.5px;
    color: var(--ink-soft);
  }
  .combo-addon .tag {
    background: var(--rose);
    color: var(--white);
    padding: 0 2px;
  }
  .combo-price {
    position: absolute;
    left: 382px; top: 110px;
    width: 42px; height: 32px;
    background: var(--rose);
    color: var(--white);
    font-family: Arial, sans-serif;
    font-size: 28px; line-height: 32px;
    padding-left: 2px;
  }
  .combo-price sup {
    font-size: 16px;
    vertical-align: 12px;
    line-height: 0;
  }
</style>
</head>
<body>
  <h1 class="board-title">Combos</h1>
  <div class="divider"></div>

  <div class="combo" style="left:76px; top:265px;">
    <span class="combo-number">1</span>
    <h2 class="combo-name"><span class="brand">Pelbrook</span>Cheese burger</h2>
    <p class="combo-sides">Mixed fries - 20oz Drink</p>
    <p class="combo-extra">add grilled onions FREE!</p>
    <p class="combo-addon">add bacon <span class="tag">99¢</span></p>
    <p class="combo-price">8<sup>69</sup></p>
  </div>
  <div class="combo" style="left:635px; top:262px;">
    <span class="combo-number">2</span>
    <h2 class="combo-name"><span class="brand">Pelbrook</span>Cheese burger</h2>
    <p class="combo-sides">Mixed fries - 20oz Drink</p>
    <p class="combo-extra">add grilled onions FREE!</p>
    <p class="combo-addon">add bacon <span class="tag">99¢</span></p>
    <p class="combo-price">8<sup>69</sup></p>
  </div>
  <div class="combo" style="left:76px; top:439px;">
    <span class="combo-number">3</span>
    <h2 class="combo-name"><span class="brand">Pelbrook</span>Cheese burger</h2>
    <p class="combo-sides">Mixed fries - 20oz Drink</p>
    <p class="combo-extra">add grilled onions FREE!</p>
    <p class="combo-addon">add bacon <span class="tag">99¢</span></p>
    <p class="combo-price">8<sup>69</sup></p>
  </div>
  <div class="combo" style="left:635px; top:437px;">
    <span class="combo-number">4</span>
    <h2 class="combo-name"><span class="brand">Pelbrook</span>Cheese burger</h2>
    <p class="combo-sides">Mixed fries - 20oz Drink</p>
    <p class="combo-extra">add grilled onions FREE!</p>
    <p class="combo-addon">add bacon <span class="tag">99¢</span></p>
    <p class="combo-price">8<sup>69</sup></p>
  </div>
  <div class="combo" style="left:76px; top:618px;">
    <span class="combo-number">5</span>
    <h2 class="combo-name"><span class="brand">Pelbrook</span>Cheese burger</h2>
    <p class="combo-sides">Mixed fries - 20oz Drink</p>
    <p class="combo-extra">add grilled onions FREE!</p>
    <p class="combo-addon">add bacon <span class="tag">99¢</span></p>
    <p class="combo-price">8<sup>69</sup></p>
  </div>
  <div class="combo" style="left:635px; top:615px;">
    <span class="combo-number">6</span>
    <h2 class="combo-name"><span class="brand">Pelbrook</span>Cheese burger</h2>
    <p class="combo-sides">Mixed fries - 20oz Drink</p>
    <p class="combo-extra">add grilled onions FREE!</p>
    <p class="combo-addon">add bacon <span class="tag">99¢</span></p>
    <p class="combo-price">8<sup>69</sup></p>
  </div>
  <div class="combo" style="left:81px; top:799px;">
    <span class="combo-number">7</span>
    <h2 class="combo-name"><span class="brand">Pelbrook</span>Cheese burger</h2>
    <p class="combo-sides">Mixed fries - 20oz Drink</p>
    <p class="combo-extra">add grilled onions FREE!</p>
    <p class="combo-addon">add bacon <span class="tag">99¢</span></p>
    <p class="combo-price">8<sup>69</sup></p>
  </div>
  <div class="combo" style="left:640px; top:797px;">
    <span class="combo-number">8</span>
    <h2 class="combo-name"><span class="brand">Pelbrook</span>Cheese burger</h2>
    <p class="combo-sides">Mixed fries - 20oz Drink</p>
    <p class="combo-extra">add grilled onions FREE!</p>
    <p class="combo-addon">add bacon <span class="tag">99¢</span></p>
    <p class="combo-price">8<sup>69</sup></p>
  </div>
  <div class="combo" style="left:361px; top:1012px;">
    <span class="combo-number">9</span>
    <h2 class="combo-name"><span class="brand">Pelbrook</span>Cheese burger</h2>
    <p class="combo-sides">Mixed fries - 20oz Drink</p>
    <p class="combo-extra">add grilled onions FREE!</p>
    <p class="combo-addon">add bacon <span class="tag">99¢</span></p>
    <p class="combo-price">8<sup>69</sup></p>
  </div>
</body>
</html>
```